Website update for Harbor Broker Ledger & Payroll Services

Our website needs updating
www.harborbrokerledgers.com
Here are some of our latest print pieces to use as a guide?
I have also attached our graphic identity guide which includes the Pantone colors

Target Market(s)

Insurance Agencies

Industry/Entity Type

Accounting

Number of Pages Required

5+ page

```html
<!DOCTYPE html>
<html lang="en">
<head>
<meta charset="utf-8">
<title>Harbor Broker Ledger & Payroll Services</title>
<link href="https://fonts.googleapis.com/css2?family=Roboto:wght@300;400;500;700&display=swap" rel="stylesheet">
<style>
:root{
  --teal:#17a896;
  --teal-dark:#0f8777;
  --ink:#3a3f44;
  --muted:#6c7277;
  --line:#e3e6e8;
  --footer:#2b3034;
  --footer-deep:#14171a;
  --white:#ffffff;
}
*{box-sizing:border-box;margin:0;padding:0}
html,body{width:711px;height:1200px;overflow:hidden;background:var(--white);font-family:'Roboto',sans-serif;color:var(--ink)}
.page{width:711px;height:1200px;position:relative}
.topbar{height:28px;border-bottom:1px solid var(--line);display:flex;align-items:center;justify-content:space-between;padding:0 48px;font-size:10px;color:var(--muted)}
.topbar .social{display:flex;gap:12px}
.dot{width:9px;height:9px;border-radius:50%;background:var(--teal)}
.topbar .mail{display:flex;align-items:center;gap:5px}
.header{height:67px;display:flex;align-items:center;justify-content:space-between;padding:0 48px}
.brand{display:flex;align-items:center;gap:8px}
.brand .mark{width:30px;height:30px;background:var(--teal)}
.brand .name{font-size:15px;font-weight:700;color:var(--teal);line-height:1.05;width:160px}
.nav{display:flex;gap:15px;font-size:10.5px}
.nav a{color:var(--ink);text-decoration:none}
.nav a.active{color:var(--teal)}
.hero{height:285px;position:relative;background:linear-gradient(135deg,#dfe7ee 0%,#b9c7d4 45%,#eef2f5 70%,#a8b6c3 100%)}
.arrow{position:absolute;top:118px;width:28px;height:48px;background:var(--teal);display:flex;align-items:center;justify-content:center}
.arrow.left{left:0}.arrow.right{right:0}
.about{text-align:center;padding:20px 60px 0}
h2{font-weight:300;font-size:30px;color:var(--teal)}
.about p{font-size:11px;line-height:1.6;color:var(--muted);text-align:left;margin:10px 0 0;padding:0 18px}
.btn{display:inline-block;border:1px solid var(--teal);color:var(--teal);font-size:11px;padding:7px 24px;margin-top:36px}
.cards{display:flex;gap:18px;padding:24px 42px 0}
.card{flex:1}
.card .photo{height:125px;background:linear-gradient(135deg,#c9d6df,#8ea3b3)}
.card .photo.blue{background:linear-gradient(135deg,#9fd3e8,#3c8fc0)}
.card .photo.office{background:linear-gradient(135deg,#e9ecef,#7c8790)}
.card h3{font-size:12.5px;font-weight:400;color:var(--teal);margin-top:10px}
.card p{font-size:9px;line-height:1.45;color:var(--muted);margin-top:6px}
.card a{display:block;font-size:9.5px;color:var(--teal);margin-top:5px}
.team{text-align:center;padding:48px 60px 0}
.team h4{font-size:19px;font-weight:300;line-height:1.35;color:var(--ink)}
.team p{font-size:10px;color:var(--muted);margin-top:8px;line-height:1.5}
.team .btn{margin-top:18px}
.footer{position:absolute;left:0;top:978px;width:711px;height:189px;background:var(--footer);border-top:4px solid var(--teal);display:flex;padding:18px 46px 0;gap:22px;color:#cfd4d8}
.footer h5{font-size:17px;font-weight:400;color:var(--white);margin-bottom:10px}
.contact{width:195px}
.row{display:flex;gap:7px;font-size:8.5px;line-height:1.4;margin-bottom:8px;align-items:flex-start}
.row svg{flex:none;margin-top:1px}
.map{width:185px;height:130px;margin-top:12px;background:linear-gradient(160deg,#e8e4da,#cfd8c6)}
.news{flex:1}
.news p{font-size:8.5px;margin-bottom:6px}
.signup{display:flex;height:22px}
.signup .field{flex:1;background:var(--white);font-size:8.5px;color:#999;padding:5px 6px}
.signup .go{width:24px;background:var(--teal)}
.news .follow{margin-top:12px;font-size:9px}
.news .social{display:flex;gap:8px;margin-top:6px}
.news .social .dot{width:16px;height:16px;background:#cfd4d8}
.bottom{position:absolute;left:0;top:1167px;width:711px;height:33px;background:var(--footer-deep);color:#aab0b5;font-size:9px;display:flex;align-items:center;justify-content:center}
</style>
</head>
<body>
<div class="page">
  <div class="topbar">
    <div class="social"><span class="dot"></span><span class="dot"></span><span class="dot"></span></div>
    <div class="mail">
      <svg width="11" height="8" viewBox="0 0 11 8"><rect x=".5" y=".5" width="10" height="7" fill="none" stroke="#17a896"/><path d="M.5 .5 5.5 4.5 10.5 .5" fill="none" stroke="#17a896"/></svg>
      info@harborbrokerledgers.com
    </div>
  </div>
  <header class="header">
    <div class="brand"><span class="mark"></span><span class="name">Harbor Broker Ledger &amp; Payroll Services</span></div>
    <nav class="nav">
      <a class="active">Home</a><a>About Us</a><a>Compare</a><a>Our Services</a><a>How it Works</a><a>Resources</a><a>Blog</a><a>Contact Us</a>
    </nav>
  </header>
  <section class="hero" role="img" aria-label="Photo of a team reviewing financial reports with calculators and pens on a desk">
    <div class="arrow left"><svg width="12" height="12" viewBox="0 0 12 12"><path d="M6 2 2 6l4 4M10 2 6 6l4 4" fill="none" stroke="#fff" stroke-width="1.6"/></svg></div>
    <div class="arrow right"><svg width="12" height="12" viewBox="0 0 12 12"><path d="M6 2l4 4-4 4M2 2l4 4-4 4" fill="none" stroke="#fff" stroke-width="1.6"/></svg></div>
  </section>
  <section class="about">
    <h2>About Us</h2>
    <p>Marla Stenwick is an Accounting Professional with more than 30 years experience in accounting, budgeting and financial reporting for independent insurance agencies. She has a proven track record of improving efficiency in agency bookkeeping and implementing technology initiatives throughout her career.</p>
    <span class="btn">Read More</span>
  </section>
  <section class="cards">
    <div class="card">
      <div class="photo" role="img" aria-label="Photo of hands working on paperwork"></div>
      <h3>Book keeping tasks</h3>
      <p>Direct bill commission deposits reconciled and recorded each month on time</p>
      <a>Read More</a>
    </div>
    <div class="card">
      <div class="photo blue" role="img" aria-label="Photo of financial charts and a calculator"></div>
      <h3>Financial statements prepared</h3>
      <p>Balance Sheet, Income Statement (compared with prior and budget).</p>
      <a>Read More</a>
    </div>
    <div class="card">
      <div class="photo office" role="img" aria-label="Photo of a business team in an office"></div>
      <h3>Sample of special projects</h3>
      <p>Clean up of general ledger accounts. Temporary assistance during staff transition</p>
      <a>Read More</a>
    </div>
  </section>
  <section class="team">
    <h4>Experienced team of insurance agency bookkeeping professionals<br>maintaining your books</h4>
    <p>Affordable, professional services for less than the cost of an in-house<br>bookkeeper and Capabilities</p>
    <span class="btn">Learn More</span>
  </section>
  <footer class="footer">
    <div class="contact">
      <h5>Keep in Touch</h5>
      <div class="row"><svg width="9" height="12" viewBox="0 0 9 12"><path d="M4.5 11.5S.5 7 .5 4.5a4 4 0 0 1 8 0C8.5 7 4.5 11.5 4.5 11.5z" fill="#17a896"/><circle cx="4.5" cy="4.5" r="1.5" fill="#2b3034"/></svg><span>Harbor Broker Ledger &amp; Payroll Services<br>42 Quayside Lane<br>Fairhaven, CT 06500</span></div>
      <div class="row"><svg width="10" height="10" viewBox="0 0 10 10"><path d="M2 .5 4 3 3 4.3a6 6 0 0 0 2.7 2.7L7 6l2.5 2L8 9.5C4 9.5.5 6 .5 2z" fill="#17a896"/></svg><span>555-014-2290</span></div>
      <div class="row"><svg width="10" height="10" viewBox="0 0 10 10"><path d="M2 .5 4 3 3 4.3a6 6 0 0 0 2.7 2.7L7 6l2.5 2L8 9.5C4 9.5.5 6 .5 2z" fill="#17a896"/></svg><span>555-014-7731</span></div>
      <div class="row"><svg width="11" height="8" viewBox="0 0 11 8"><rect x=".5" y=".5" width="10" height="7" fill="none" stroke="#17a896"/><path d="M.5 .5 5.5 4.5 10.5 .5" fill="none" stroke="#17a896"/></svg><span>info@harborbrokerledgers.com</span></div>
    </div>
    <div class="map" role="img" aria-label="Map showing the office location"></div>
    <div class="news">
      <h5>NewsLetter</h5>
      <p>Signup here for our email update</p>
      <div class="signup"><span class="field">Email Id</span><span class="go"></span></div>
      <div class="follow">Follow Us</div>
      <div class="social"><span class="dot"></span><span class="dot"></span><span class="dot"></span></div>
    </div>
  </footer>
  <div class="bottom">© HBLP Services - 2015. All rights reserved.</div>
</div>
</body>
</html>
```